Tally Shift GUI Contest

Hello everyone. I want a unique design for my app "Tally Shift". Now, I published this app to Bramble Shelf.

(Please see https://shelf.bramblo.example/apps/view?id=com.korvane.tallyshift&feature=search_result#?t=QmxvcnZhbmVUYWxseVNoaWZ0WA )

Now, I got a lot of negative responds for UI. So, I really need beautiful UI for this app.

Please see attachment. I like that kind of framework.

I don't like Side by Side display. I like Currency and Country shows vertically.

I will add Banner at the bottom of screen too. So, make sure give enough space for banner ,if not your UI design will be ugly due to this.

Please see my attached files. These are screenshots of my current UI design for Tally Shift. You can reference these screenshots if you don't have android devices to test.

Rotate icon at the center of screen is to reverse country. :)

Target Market(s)

Android

Industry/Entity Type

Store

Requirements
Must have
• Colorful
Screen Size (320 x 480 or 480 x 800 or 480 x 854 or 1280 x 720 and 1280 x 800)
Nice to have
• I attached sample template file. I don't mean that UI design may be similar like this. You can design as you like. You can use any color. If it is beautiful in my eye, I will choose. If I like two designs, I will choose 2nd winner too.

I really need eye catching design.
Should not have
• I hate Side by Side currency display. (https://shelf.bramblo.example/apps/view?id=com.pemlo.tallyplus.quindar&feature=search_result#?t=UGVtbG9UYWxseVBsdXNRdWluZGFyWlo.)

```html
<!DOCTYPE html>
<html lang="en">
<head>
<meta charset="utf-8">
<title>Tally Shift</title>
<link rel="stylesheet" href="https://fonts.googleapis.com/css2?family=Mulish:wght@400;700;800&display=swap">
<style>
  :root {
    --canvas: #ffffff;
    --screen: #000000;
    --panel: #3a3a3a;
    --panel-deep: #2a2a2a;
    --bar-top: #8a8a8a;
    --bar-bottom: #3c3c3c;
    --accent: #f5b800;
    --text: #eeeeee;
    --label: #bdbdbd;
    --stamp: #2aa3de;
    --ad-bg: #2e2e2e;
    --ad-pink: #d10d5a;
    --flag-blue: #3c4f9a;
    --flag-red: #c8202f;
    --flag-white: #eeeeee;
    --flag-yellow: #f5c300;
    --flag-green: #35a047;
  }
  * { box-sizing: border-box; margin: 0; padding: 0; }
  html, body { width: 1200px; height: 901px; overflow: hidden; }
  body { background: var(--canvas); font-family: "Mulish", sans-serif; position: relative; }

  .app-screen { position: absolute; left: 459px; top: 148px; width: 346px; height: 587px; background: var(--screen); overflow: hidden; }

  .status-bar { position: absolute; left: 0; top: 0; width: 100%; height: 35px; color: #fff; }
  .status-bar .signal { position: absolute; left: 10px; top: 10px; }
  .status-bar .battery { position: absolute; right: 50px; top: 12px; }
  .status-bar .clock { position: absolute; right: 2px; top: 9px; font-size: 13px; line-height: 16px; }

  .toolbar { position: absolute; left: 0; top: 35px; width: 100%; height: 36px;
    background: linear-gradient(var(--bar-top), var(--bar-bottom));
    border-bottom: 1px solid var(--accent); display: flex; }
  .toolbar .tool { flex: 1; display: flex; align-items: center; justify-content: center; }
  .toolbar .tool + .tool { border-left: 1px solid #2a2a2a; }

  .label { position: absolute; left: 0; width: 100%; text-align: center; font-size: 14px; line-height: 18px; color: var(--label); }

  .amount-strip { position: absolute; left: 0; top: 72px; width: 100%; height: 26px; background: var(--panel); }
  .amount-strip .label { top: 3px; }
  .amount-field { position: absolute; left: 0; top: 98px; width: 100%; height: 46px; background: var(--panel-deep);
    display: flex; align-items: center; justify-content: center; font-weight: 800; font-size: 30px; color: var(--text); }

  .currency-panel { position: absolute; left: 0; top: 146px; width: 100%; height: 292px; background: var(--panel); }
  .currency-row { position: absolute; left: 24px; width: 298px; height: 28px; display: flex; align-items: center; }
  .currency-row .name { margin-left: 10px; font-weight: 700; font-size: 20px; color: var(--text); flex: 1; white-space: nowrap; }
  .currency-row .flag { width: 34px; height: 25px; display: block; }
  .swap-button { position: absolute; left: 138px; top: 83px; }
  .stamp { position: absolute; left: 0; top: 417px; width: 100%; display: flex; justify-content: center; gap: 18px;
    font-size: 14px; line-height: 18px; color: var(--stamp); }

  .result-field { position: absolute; left: 0; top: 440px; width: 100%; height: 100px; background: var(--panel-deep);
    display: flex; align-items: center; justify-content: center; font-weight: 800; font-size: 50px; color: var(--text); }

  .banner-slot { position: absolute; left: 0; top: 542px; width: 100%; height: 45px; background: var(--panel); border-top: 1px solid var(--accent); }
  .ad { position: absolute; left: 35px; top: 0; width: 276px; height: 44px; background: var(--ad-bg); display: flex; align-items: center; }
  .ad .brand { margin-left: 14px; font-weight: 700; font-size: 19px; color: var(--text); }
  .ad .tagline { margin-left: 10px; font-size: 12px; line-height: 13px; color: var(--label); }
  .ad .cta { margin-left: auto; width: 97px; height: 100%; background: var(--ad-pink); color: #fff; font-size: 12px; line-height: 13px;
    display: flex; align-items: center; padding-left: 9px; gap: 10px; }
</style>
</head>
<body>
  <main class="app-screen">
    <div class="status-bar">
      <svg class="signal" width="22" height="14" viewBox="0 0 22 14" fill="#fff">
        <rect x="0" y="10" width="3" height="4"/><rect x="5" y="7" width="3" height="7"/><rect x="10" y="4" width="3" height="10"/><rect x="15" y="0" width="3" height="14"/>
      </svg>
      <svg class="battery" width="24" height="11" viewBox="0 0 24 11">
        <rect x="0.5" y="0.5" width="20" height="10" fill="none" stroke="#fff"/><rect x="2" y="2" width="17" height="7" fill="#fff"/><rect x="21" y="3" width="2" height="5" fill="#fff"/>
      </svg>
      <span class="clock">10:08</span>
    </div>

    <nav class="toolbar">
      <div class="tool" aria-label="About">
        <svg width="20" height="20" viewBox="0 0 20 20" fill="none" stroke="var(--accent)" stroke-width="2">
          <circle cx="10" cy="10" r="8"/><line x1="10" y1="9" x2="10" y2="15"/><line x1="10" y1="5" x2="10" y2="7"/>
        </svg>
      </div>
      <div class="tool" aria-label="Refresh rates">
        <svg width="20" height="20" viewBox="0 0 20 20" fill="none" stroke="var(--accent)" stroke-width="2.2">
          <path d="M16 10a6 6 0 1 1-3-5.2"/><path d="M11 2.5l3 2.3-2.6 2.7" stroke-linejoin="round"/>
        </svg>
      </div>
    </nav>

    <div class="amount-strip"><p class="label">amount</p></div>
    <div class="amount-field">8196.75</div>

    <section class="currency-panel">
      <p class="label" style="top:8px">from</p>
      <div class="currency-row" style="top:28px">
        <svg width="19" height="12" viewBox="0 0 19 12" fill="var(--accent)"><rect width="19" height="2"/><rect y="5" width="19" height="2"/><rect y="10" width="19" height="2"/></svg>
        <span class="name">(USD) U.S. Dollar</span>
        <svg class="flag" viewBox="0 0 34 25" role="img" aria-label="United States flag">
          <rect width="34" height="25" fill="var(--flag-white)"/>
          <g fill="var(--flag-red)"><rect y="0" width="34" height="2"/><rect y="4" width="34" height="2"/><rect y="8" width="34" height="2"/><rect y="12" width="34" height="2"/><rect y="16" width="34" height="2"/><rect y="20" width="34" height="2"/><rect y="23" width="34" height="2"/></g>
          <rect width="15" height="13" fill="var(--flag-blue)"/>
        </svg>
      </div>

      <svg class="swap-button" width="70" height="70" viewBox="0 0 70 70" fill="none" stroke="var(--accent)" stroke-width="7" aria-label="Swap currencies">
        <path d="M15 28A22 22 0 0 1 53 20"/><path d="M55 42A22 22 0 0 1 17 50"/>
        <path d="M58 8v17H41z" fill="var(--accent)" stroke="none"/><path d="M12 62V45h17z" fill="var(--accent)" stroke="none"/>
      </svg>

      <p class="label" style="top:175px">to</p>
      <div class="currency-row" style="top:195px">
        <svg width="19" height="12" viewBox="0 0 19 12" fill="var(--accent)"><rect width="19" height="2"/><rect y="5" width="19" height="2"/><rect y="10" width="19" height="2"/></svg>
        <span class="name">(MMK) Myanmar Kyat</span>
        <svg class="flag" viewBox="0 0 34 25" role="img" aria-label="Myanmar flag">
          <rect width="34" height="9" fill="var(--flag-yellow)"/><rect y="8" width="34" height="9" fill="var(--flag-green)"/><rect y="16" width="34" height="9" fill="var(--flag-red)"/>
          <path d="M17 5l2 5.5h5.5l-4.5 3.3 1.8 5.5-4.8-3.4-4.8 3.4 1.8-5.5-4.5-3.3h5.5z" fill="#fff"/>
        </svg>
      </div>

      <p class="label" style="top:256px">converted amount</p>
    </section>
    <p class="stamp"><span>21.03.2013</span><span>10:23 PM</span></p>

    <div class="result-field">11362.48</div>

    <footer class="banner-slot">
      <div class="ad">
        <span class="brand">Chirpa</span>
        <span class="tagline">Instant<br>Messenger</span>
        <span class="cta">Download<br>free app
          <svg width="13" height="9" viewBox="0 0 13 9" fill="#fff"><path d="M0 0h13L6.5 9z"/></svg>
        </span>
      </div>
    </footer>
  </main>
</body>
</html>
```